I am looking for a Business Card Design for my spirit company titled "Harbor Pour Co" The company specializes in prohibition style/speakeasy mixology drinks and alcohol distribution. I am looking for Retro, Masculine, Sophisticated Card that embodies the look of Prohibition. Black and White colors. Also add Facebook, Instgram logo

Information that should go on the card is my Name, Title, Phone, Email, Website as follows:

Tobias K Verran
Principal
301.555.0187
tobias@harborpourco.example
harborpourco.example
Updates

Hello all I have uploaded a pdf version of the logo. It seems as if some are saying the resolution is too small.

Target Market(s)

Male and Female drinkers of all ages with a sophisticated palate that have an appreciation for fine crafted cocktail

Industry/Entity Type

Business

Requirements
Must have
• Information that should go on the card is my Name, Title, Phone, Email, Website as follows:

Tobias K Verran
Principal
301.555.0187
tobias@harborpourco.example
harborpourco.example

```html
<!DOCTYPE html>
<html lang="en">
<head>
<meta charset="utf-8">
<title>Harbor Pour Co — Business Card</title>
<link rel="stylesheet" href="https://fonts.googleapis.com/css2?family=Libre+Bodoni:wght@400;700&display=swap">
<style>
  :root {
    --page: #ffffff;
    --ink: #0a0a0a;
    --card-dark: #161616;
    --glass-mid: #3a3a3a;
    --glass-light: #ffffff;
    --back-shadow: #262626;
    --text-light: #ffffff;
  }
  * { box-sizing: border-box; margin: 0; padding: 0; }
  html, body {
    width: 1070px;
    height: 1200px;
    overflow: hidden;
    background: var(--page);
  }
  .sheet {
    position: relative;
    width: 1070px;
    height: 1200px;
  }
  .card {
    position: absolute;
    left: 59px;
    width: 944px;
    height: 540px;
    overflow: hidden;
    background: var(--card-dark);
  }
  .card--front { top: 56px; }
  .card--back { top: 609px; }

  .front-art {
    position: absolute;
    inset: 0;
    background: radial-gradient(ellipse 300px 290px at 50% 50%,
      var(--glass-light) 0%, var(--glass-light) 78%,
      #9a9a9a 88%, var(--glass-mid) 96%, var(--card-dark) 100%);
  }
  .wordmark {
    position: absolute;
    left: 0;
    right: 0;
    top: 168px;
    text-align: center;
    font-family: "Libre Bodoni", serif;
    font-weight: 400;
    font-size: 76px;
    line-height: 1;
    color: var(--ink);
  }
  .wordmark span { display: block; }

  .back-art {
    position: absolute;
    inset: 0;
    background:
      radial-gradient(circle 190px at 63% 30%, var(--back-shadow) 0%, var(--back-shadow) 90%, transparent 100%),
      radial-gradient(circle 210px at 29% 62%, var(--back-shadow) 0%, var(--back-shadow) 90%, transparent 100%),
      var(--card-dark);
  }
  .contact {
    position: absolute;
    left: 75px;
    top: 268px;
    font-family: "Libre Bodoni", serif;
    color: var(--text-light);
  }
  .contact__name {
    font-weight: 700;
    font-size: 45px;
    line-height: 1;
    letter-spacing: -0.6px;
  }
  .contact__title {
    font-weight: 700;
    font-size: 24px;
    line-height: 1.1;
    margin-bottom: 22px;
  }
  .contact__line {
    font-weight: 700;
    font-size: 25px;
    line-height: 1.4;
    letter-spacing: -0.4px;
  }
</style>
</head>
<body>
<main class="sheet">
  <section class="card card--front">
    <div class="front-art" role="img" aria-label="Shattered black glass surrounding a bright white circular opening"></div>
    <h1 class="wordmark"><span>Harbor</span><span>Pour Co</span></h1>
  </section>

  <section class="card card--back">
    <div class="back-art" role="img" aria-label="Faint dark shattered glass impacts across a black background"></div>
    <div class="contact">
      <h2 class="contact__name">Tobias K Verran</h2>
      <p class="contact__title">Principal</p>
      <p class="contact__line">301.555.0187</p>
      <p class="contact__line">tobias@harborpourco.example</p>
      <p class="contact__line">harborpourco.example</p>
    </div>
  </section>
</main>
</body>
</html>
```